Company providing wellness products (skin care, herbal, soap) needs website design.

Our company name is Silver Heron Acres and we provide wellness products for our customers. We also provide organically grown vegetables and herbs. Our website is on Wix and we have the basic layout completed; however, we need a better design. I assume this means that we can import the designs that you provide into the Wix environment. If this is not true, we do not want to move forward with the project. I included a copy of a logo that was done by your team.

Target Market(s)

women with income exceeded 75k interested in health and natural products.

Industry/Entity Type

Skin Care Product

Number of Pages Required

5+ page

Font styles to use
Serif
Sans Serif
Decorative
Script

Requirements
Must have
• Not sure of the number of pages as I really need a theme designed that I can carry throughout the site.
Nice to have
• clean, fresh, organic sophisticated feel. I would like to incorporate our logo that I attached. We are open to a different logo if it works better with your design. Our name is Silver Heron Acres and our logo is green so I think green should be incorporated but are open to what you design.

```html
<!DOCTYPE html>
<html lang="en">
<head>
<meta charset="utf-8">
<title>Silver Heron Acres</title>
<link rel="stylesheet" href="https://fonts.googleapis.com/css2?family=Montserrat:wght@400;500;600;700;800&family=IBM+Plex+Sans:wght@400;500&display=swap">
<style>
:root{
  --green:#5f9a2f;
  --ink:#1d1d1d;
  --text:#3a3a3a;
  --panel:#e4e4e6;
  --footer:#1d191a;
  --white:#ffffff;
}
*{box-sizing:border-box;margin:0;padding:0}
html,body{width:1200px;height:3562px;overflow:hidden}
body{position:relative;background:var(--white);font-family:"IBM Plex Sans",Arial,sans-serif;color:var(--text)}
.btn{position:absolute;display:flex;align-items:center;justify-content:center;background:var(--green);color:var(--white);font-family:"Montserrat",Arial,sans-serif;font-weight:700;text-transform:uppercase;text-decoration:none}
.btn.light{background:var(--white);color:var(--green)}

/* header */
.site-header{position:absolute;left:0;top:0;width:1200px;height:110px;background:var(--white)}
.brand-dot{position:absolute;left:131px;top:33px;width:26px;height:26px;border-radius:50%;background:var(--green)}
.brand{position:absolute;left:166px;top:35px;font-family:"Montserrat",sans-serif;font-weight:600;font-size:18px;color:var(--ink);white-space:nowrap}
.follow{position:absolute;left:736px;top:27px;font-family:"Montserrat",sans-serif;font-size:13px;color:var(--ink)}
.social-dot{position:absolute;top:24px;width:23px;height:23px;border-radius:50%;background:#2c5fb5}
.call-icon{position:absolute;left:919px;top:24px;width:28px;height:28px;border-radius:50%;border:1.5px solid var(--ink)}
.call{position:absolute;left:957px;top:19px;font-family:"Montserrat",sans-serif;font-size:12px;color:var(--ink);line-height:1.2}
.call b{font-size:16px;font-weight:600}
.nav a{position:absolute;top:72px;font-family:"Montserrat",sans-serif;font-weight:500;font-size:15px;color:var(--ink);text-decoration:none}
.nav a.active{color:var(--green);font-weight:700;border-bottom:2px solid var(--green);padding-bottom:1px}

/* hero */
.hero{position:absolute;left:0;top:110px;width:1200px;height:558px;background:radial-gradient(ellipse at 72% 55%,#6b5436 0%,#3e4a2a 30%,#263620 60%,#1c2a18 100%)}
.hero h1{position:absolute;left:130px;top:138px;font-family:"Montserrat",sans-serif;font-weight:800;font-size:56px;color:var(--white);letter-spacing:1px}
.hero p{position:absolute;left:130px;top:214px;width:400px;font-family:"Montserrat",sans-serif;font-size:20px;line-height:29px;color:var(--white)}
.dots span{position:absolute;top:520px;width:7px;height:7px;border-radius:50%;background:var(--white)}

.sec-title{position:absolute;left:0;width:1200px;text-align:center;font-family:"Montserrat",sans-serif;font-weight:700;font-size:19px;color:var(--ink)}
.rule{position:absolute;left:584px;width:40px;height:2px;background:#9a9a9a}

/* product cards */
.product{position:absolute;top:783px;width:364px;height:445px;background:var(--white);box-shadow:0 4px 14px rgba(0,0,0,.09)}
.product .photo{height:276px}
.product h3{position:absolute;top:302px;width:100%;text-align:center;font-family:"Montserrat",sans-serif;font-weight:700;font-size:16px;color:var(--ink)}
.product p{position:absolute;top:334px;width:100%;text-align:center;font-size:13px;line-height:20px;color:var(--ink)}
.product .btn{left:138px;top:392px;width:87px;height:27px;font-size:9px}

/* welcome */
.welcome{position:absolute;left:0;top:1284px;width:1200px;height:448px;background:var(--panel)}
.welcome .emblem-name{position:absolute;left:120px;top:202px;width:390px;text-align:center;font-family:"Montserrat",sans-serif;font-weight:700;font-size:32px;color:var(--ink)}
.welcome .divider{position:absolute;left:536px;top:52px;width:1px;height:352px;background:#c4c4c4}
.welcome .kicker{position:absolute;left:621px;top:60px;font-family:"Montserrat",sans-serif;font-weight:700;font-size:15px;color:#333}
.welcome h2{position:absolute;left:621px;top:82px;font-family:"Montserrat",sans-serif;font-weight:700;font-size:22px;color:#3a3a3a}
.welcome .wrule{position:absolute;left:621px;top:119px;width:80px;height:2px;background:#999}
.welcome p{position:absolute;left:622px;top:155px;width:448px;font-size:15.5px;line-height:22.5px;color:#444}
.welcome .btn{left:625px;top:353px;width:112px;height:36px;font-size:12.5px}

/* bands */
.band{position:absolute;left:0;width:1200px}
.band-veg{top:1732px;height:488px;background:linear-gradient(90deg,#33482a 0%,#5a6b3f 30%,#a9b3a5 55%,#7a4248 80%,#3a3038 100%)}
.band-veg h2{position:absolute;left:131px;top:140px;font-family:"Montserrat",sans-serif;font-weight:800;font-size:28px;line-height:34px;color:var(--white)}
.band-veg p{position:absolute;left:132px;top:232px;width:310px;font-size:17px;line-height:21.5px;color:var(--white)}
.band-veg .btn{left:131px;top:368px;width:111px;height:36px;font-size:12.5px}

/* blog */
.post{position:absolute;top:2335px;width:298px;height:362px;background:var(--white);border:1px solid #dcdcdc}
.post .photo{height:167px}
.post .date{position:absolute;left:22px;top:160px;padding:3px 8px;background:var(--white);font-size:11px;color:var(--ink)}
.post h3{position:absolute;left:22px;top:192px;width:260px;font-family:"Montserrat",sans-serif;font-weight:700;font-size:14.5px;line-height:18px;color:var(--ink)}
.post p{position:absolute;left:22px;top:242px;width:262px;font-size:11.5px;line-height:18px;color:#333}
.post .btn{left:24px;top:309px;width:86px;height:24px;font-size:9.5px}

.band-herbs{top:2750px;height:470px;background:radial-gradient(ellipse at 50% 50%,#3f6a2d 0%,#2c4e20 50%,#1c3416 100%)}
.band-herbs h2{position:absolute;left:0;top:132px;width:1200px;text-align:center;font-family:"Montserrat",sans-serif;font-weight:800;font-size:30px;color:var(--white)}
.band-herbs p{position:absolute;left:290px;top:196px;width:620px;text-align:center;font-size:19px;line-height:26.5px;color:var(--white)}
.band-herbs .btn{left:536px;top:301px;width:126px;height:42px;font-size:14px}

/* footer */
.site-footer{position:absolute;left:0;top:3220px;width:1200px;height:342px;background:var(--footer);color:var(--white)}
.foot-dot{position:absolute;left:128px;top:127px;width:30px;height:30px;border-radius:50%;background:var(--white)}
.foot-brand{position:absolute;left:168px;top:124px;font-family:"Montserrat",sans-serif;font-weight:600;font-size:28px;line-height:36px;white-space:nowrap}
.foot-col h4{position:absolute;top:56px;font-family:"Montserrat",sans-serif;font-weight:700;font-size:13px}
.foot-menu{position:absolute;left:442px;top:92px;list-style:none;font-size:12px;line-height:20px}
.foot-item{position:absolute;font-size:11.5px;line-height:15px}
.foot-icon{position:absolute;width:22px;height:22px;border-radius:50%;background:var(--white)}
.foot-line{position:absolute;left:122px;top:268px;width:956px;height:1px;background:#4a4546}
.copyright{position:absolute;left:0;top:302px;width:1200px;text-align:center;font-size:9.5px;color:#ddd}
</style>
</head>
<body>

<header class="site-header">
  <div class="brand-dot"></div>
  <div class="brand">Silver Heron Acres</div>
  <div class="follow">Follow us</div>
  <span class="social-dot" style="left:807px"></span>
  <span class="social-dot" style="left:838px;background:#1d9bf0"></span>
  <span class="social-dot" style="left:869px;background:#1b2a6b"></span>
  <div class="call-icon">
    <svg width="25" height="25" viewBox="0 0 24 24"><path d="M8.5 7.5c.6 2.8 2.6 5.4 5.6 6.8l1.4-1.4 2 1.1-.6 1.8c-4.4-.2-8.4-4-8.9-8.5l1.6-.6z" fill="none" stroke="#1d1d1d" stroke-width="1.2"/></svg>
  </div>
  <div class="call">Call us<br><b>555.014.2290</b></div>
  <nav class="nav">
    <a class="active" style="left:420px">HOME</a>
    <a style="left:511px">ABOUT US</a>
    <a style="left:637px">SERVICES</a>
    <a style="left:759px">PRODUCTS</a>
    <a style="left:891px">BLOG</a>
    <a style="left:973px">CONTACT US</a>
  </nav>
</header>

<section class="hero" role="img" aria-label="Wooden mortar and pestle filled with fresh green herbs on a blurred garden background">
  <h1>HERBAL</h1>
  <p>Lorem Ipsum is simply dummy text of the printing and typesetting.</p>
  <a class="btn" style="left:133px;top:298px;width:139px;height:43px;font-size:15px">Read More</a>
  <div class="dots">
    <span style="left:562px"></span><span style="left:579px"></span><span style="left:597px;background:var(--green)"></span><span style="left:615px"></span><span style="left:632px"></span>
  </div>
</section>

<h2 class="sec-title" style="top:707px">OUR PRODUCTS</h2>
<div class="rule" style="top:745px"></div>

<article class="product" style="left:33px">
  <div class="photo" role="img" aria-label="White skin care bottles, tube and jar on a light table" style="background:linear-gradient(180deg,#eeeeee 0%,#e2dfdc 70%,#cdb89e 100%)"></div>
  <h3>SKIN CARE</h3>
  <p>Lorem Ipsum is simply dummy text of<br>the printing and typesetting .</p>
  <a class="btn">Read More</a>
</article>
<article class="product" style="left:420px">
  <div class="photo" role="img" aria-label="White mortar and pestle with fresh herbs on a green background" style="background:radial-gradient(circle at 50% 60%,#e8ede4 0%,#57a32f 45%,#2f7d1d 100%)"></div>
  <h3>HERBAL</h3>
  <p>Lorem Ipsum is simply dummy text of<br>the printing and typesetting .</p>
  <a class="btn">Read More</a>
</article>
<article class="product" style="left:805px">
  <div class="photo" role="img" aria-label="Handmade soap bars tied with twine next to lavender" style="background:linear-gradient(135deg,#5c5a79 0%,#c8a46b 40%,#e7c766 60%,#8f8a86 100%)"></div>
  <h3>SOAP</h3>
  <p>Lorem Ipsum is simply dummy text of<br>the printing and typesetting .</p>
  <a class="btn">Read More</a>
</article>

<section class="welcome">
  <div class="emblem-name">Silver Heron Acres</div>
  <div class="divider"></div>
  <div class="kicker">WELCOME TO</div>
  <h2>SILVER HERON ACRES</h2>
  <div class="wrule"></div>
  <p>Sed ut perspiciatis unde omnis iste natus error sit volupt atem accusantium doloremque laudantium, totam rem aperiam, eaque ipsa quae ab illo inventore veritatis et quasi architecto beatae vitae dicta sunt explicabo. Nemo enim ipsam voluptatem quia voluptas sit aspernatur aut odit aut fugit, sed quia consequuntur magni dolores eos qui ratione voluptatem sequi nesciunt. Neque porro quisquam est,</p>
  <a class="btn">Read More</a>
</section>

<section class="band band-veg" role="img" aria-label="Person holding a wooden crate of fresh organic vegetables on a garden path">
  <h2>ORGANICALLY<br>GROWN VEGETABLES</h2>
  <p>Sed ut perspiciatis unde omnis iste natus error sit volupt atem accus an tium dolor emque laudantium, totam rem aperiam, eaque ipsa quae ab illo inventore veritatis.</p>
  <a class="btn light">Read More</a>
</section>

<h2 class="sec-title" style="top:2260px">LATEST BLOG</h2>
<div class="rule" style="top:2300px"></div>

<article class="post" style="left:131px">
  <div class="photo" role="img" aria-label="Bars of natural soap on a woven mat" style="background:linear-gradient(135deg,#a88a66 0%,#d8c48d 50%,#8c7253 100%)"></div>
  <span class="date">15/03/2021</span>
  <h3>Sed ut perspiciatis unde omnis iste natus error.</h3>
  <p>But I must explain to you how all this mistaken idea of denouncing pleasure and praising pain was born and I will give you.</p>
  <a class="btn">Read More</a>
</article>
<article class="post" style="left:452px">
  <div class="photo" role="img" aria-label="Blue cosmetic bottles on a water blue background" style="background:linear-gradient(135deg,#8fd3e6 0%,#4fb3d3 50%,#7fcbe0 100%)"></div>
  <span class="date">15/03/2021</span>
  <h3>Sed ut perspiciatis unde omnis iste natus error.</h3>
  <p>But I must explain to you how all this mistaken idea of denouncing pleasure and praising pain was born and I will give you.</p>
  <a class="btn">Read More</a>
</article>
<article class="post" style="left:773px">
  <div class="photo" role="img" aria-label="Cream jar, brush and pink flowers on a white table" style="background:linear-gradient(135deg,#e9d8da 0%,#f3eeee 50%,#d9a2ad 100%)"></div>
  <span class="date">15/03/2021</span>
  <h3>Sed ut perspiciatis unde omnis iste natus error.</h3>
  <p>But I must explain to you how all this mistaken idea of denouncing pleasure and praising pain was born and I will give you.</p>
  <a class="btn">Read More</a>
</article>

<section class="band band-herbs" role="img" aria-label="Close view of fresh green herb leaves">
  <h2>ORGANICALLY GROWN HERBS</h2>
  <p>Sed ut perspiciatis unde omnis iste natus error sit volupt atem accus an tium dolor emque laudantium, totam rem aperiam, eaque ipsa quae ab illo inventore veritatis.</p>
  <a class="btn light">Read More</a>
</section>

<footer class="site-footer">
  <div class="foot-dot"></div>
  <div class="foot-brand">Silver Heron</div>

  <div class="foot-col"><h4 style="left:442px">MENU</h4></div>
  <ul class="foot-menu">
    <li>HOME</li><li>ABOUT US</li><li>SERVICES</li><li>PRODUCTS</li><li>BLOG</li><li>CONTACT US</li>
  </ul>

  <div class="foot-col"><h4 style="left:641px">CONTACT US</h4></div>
  <span class="foot-icon" style="left:640px;top:92px">
    <svg width="22" height="22" viewBox="0 0 22 22"><path d="M11 5a4 4 0 0 0-4 4c0 3 4 7 4 7s4-4 4-7a4 4 0 0 0-4-4z" fill="#1d191a"/><circle cx="11" cy="9" r="1.4" fill="#fff"/></svg>
  </span>
  <div class="foot-item" style="left:672px;top:94px">2210 Meadowlark Road<br>Fairbrook, CA 90000</div>
  <span class="foot-icon" style="left:640px;top:144px">
    <svg width="22" height="22" viewBox="0 0 22 22"><path d="M8 6.5c.5 3 2.5 5.7 5.7 7.2l1.3-1.3 1.8 1-.5 1.7C12 15 7.8 11 7.3 7l.7-.5z" fill="#1d191a"/></svg>
  </span>
  <div class="foot-item" style="left:672px;top:147px">Call Us<br>555.014.2290</div>
  <span class="foot-icon" style="left:640px;top:196px">
    <svg width="22" height="22" viewBox="0 0 22 22"><rect x="6" y="7.5" width="10" height="7" fill="#1d191a"/><path d="M6 7.5l5 4 5-4" fill="none" stroke="#fff" stroke-width="1"/></svg>
  </span>
  <div class="foot-item" style="left:672px;top:197px">E mail Us<br>hello@SilverHeronAcres.com</div>

  <div class="foot-col"><h4 style="left:950px">FOLLOW US</h4></div>
  <span class="foot-icon" style="left:949px;top:92px"></span>
  <div class="foot-item" style="left:984px;top:94px">Like us on<br>FEEDSPACE</div>
  <span class="foot-icon" style="left:949px;top:144px"></span>
  <div class="foot-item" style="left:984px;top:147px">Follow us on<br>CHIRPLINE</div>
  <span class="foot-icon" style="left:949px;top:196px"></span>
  <div class="foot-item" style="left:984px;top:197px">Follow us on<br>LINKPATH</div>

  <div class="foot-line"></div>
  <div class="copyright">Copyright © 2021 All Rights Reserved</div>
</footer>

</body>
</html>
```